Healthcare and Professional IT Services Company need a redesigned business card

We are a IT Services company that targets small medical practices and professional business such as Attorneys, Accounts, Architects etc. We want to communicate a professional yet friendly image using recent logo redesign here on Sketchforge. Like to see the colors blue and orange in the design. Must use the Copper Lantern Technology as displayed in the new logo - then also want to incorporate the fish logo as well.

Target Market(s)

Small medical and professional services

Industry/Entity Type

It Company

Contact Information for Business Card

The usual stuff, place for name address phone website. Also maybe our tagline which is "tuned for technology"

Requirements
Must have
• My new logo and the fish somewhere on the card

```html
<!DOCTYPE html>
<html lang="en">
<head>
<meta charset="utf-8">
<title>Copper Lantern Technology – Business Card</title>
<link rel="stylesheet" href="https://fonts.googleapis.com/css2?family=Open+Sans:wght@400;600;700&display=swap">
<style>
  :root {
    --backdrop: #2b2b2d;
    --card-white: #f4f4f4;
    --card-white-edge: #d9d9d9;
    --card-blue: #0d98dc;
    --card-blue-deep: #0584c8;
    --brand-blue: #1b7fc0;
    --brand-orange: #e88a2a;
    --ink-white: #ffffff;
    --rule-light: rgba(255,255,255,0.55);
  }
  * { box-sizing: border-box; margin: 0; padding: 0; }
  html, body { width: 1200px; height: 871px; overflow: hidden; }
  body {
    background: var(--backdrop);
    font-family: "Open Sans", Arial, sans-serif;
    display: flex;
    flex-direction: column;
    align-items: center;
    justify-content: center;
    gap: 56px;
  }
  .card {
    width: 560px;
    height: 320px;
    border-radius: 4px;
    position: relative;
    overflow: hidden;
    box-shadow: 0 10px 24px rgba(0,0,0,0.45);
  }

  /* Front: logo side */
  .card--front {
    background: linear-gradient(135deg, #ffffff 0%, var(--card-white) 55%, var(--card-white-edge) 100%);
    display: flex;
    flex-direction: column;
    align-items: center;
    justify-content: center;
    gap: 12px;
  }
  .mascot-area--front {
    width: 150px;
    height: 70px;
    border-radius: 8px;
    background: rgba(27,127,192,0.14);
  }
  .brand {
    display: flex;
    align-items: center;
    gap: 12px;
  }
  .brand__dot {
    width: 20px;
    height: 20px;
    border-radius: 50%;
    background: var(--brand-orange);
  }
  .brand__name {
    font-weight: 700;
    font-size: 28px;
    color: var(--brand-blue);
    letter-spacing: -0.3px;
  }
  .tagline {
    font-weight: 600;
    font-size: 17px;
    color: var(--brand-blue);
  }

  /* Back: contact side */
  .card--back {
    background: linear-gradient(120deg, var(--card-blue-deep) 0%, var(--card-blue) 60%, #2aa9e6 100%);
    color: var(--ink-white);
    display: flex;
    flex-direction: column;
    align-items: center;
    justify-content: center;
  }
  .mascot-area--back {
    width: 130px;
    height: 70px;
    border-radius: 8px;
    background: rgba(255,255,255,0.18);
    margin-bottom: 10px;
  }
  .rule {
    width: 420px;
    height: 1px;
    background: var(--rule-light);
  }
  .contact {
    text-align: center;
    padding: 10px 0 12px;
    line-height: 1.55;
  }
  .contact__name {
    font-weight: 700;
    font-size: 19px;
  }
  .contact__role { font-weight: 600; font-size: 16px; }
  .contact__line {
    font-size: 14px;
    display: flex;
    align-items: center;
    justify-content: center;
    gap: 6px;
  }
  .contact__line svg { width: 14px; height: 14px; fill: var(--ink-white); }
  .spacer { width: 10px; }
</style>
</head>
<body>

  <section class="card card--front">
    <div class="mascot-area--front" role="img" aria-label="Brand fish mascot outline in blue"></div>
    <div class="brand">
      <span class="brand__dot"></span>
      <span class="brand__name">Copper Lantern Technology</span>
    </div>
    <p class="tagline">tuned for technology</p>
  </section>

  <section class="card card--back">
    <div class="mascot-area--back" role="img" aria-label="Brand fish mascot outline in white"></div>
    <div class="rule"></div>
    <div class="contact">
      <p class="contact__name">Mara Ellison <span class="contact__role">&nbsp;-&nbsp; President</span></p>
      <p class="contact__line">4127 Harbor Lane, Millbrook, NY 12545</p>
      <p class="contact__line">
        <svg viewBox="0 0 16 16" aria-hidden="true"><path d="M3 1h3l1.5 4-2 1.2a9 9 0 0 0 4.3 4.3L11 8.5l4 1.5v3a2 2 0 0 1-2 2A12 12 0 0 1 1 3a2 2 0 0 1 2-2z"/></svg>
        555 0142 7781
        <span class="spacer"></span>
        <svg viewBox="0 0 16 16" aria-hidden="true"><path d="M1 3h14v10H1z M1 3l7 6 7-6" stroke="#0d98dc" stroke-width="1.2"/></svg>
        mara@lanternit.net
      </p>
      <p class="contact__line">
        <svg viewBox="0 0 16 16" aria-hidden="true"><circle cx="8" cy="8" r="7"/></svg>
        www.lanternit.net
      </p>
    </div>
    <div class="rule"></div>
  </section>

</body>
</html>
```